Website for Company to help with House Restoration from Hurricane Damage

Crisp, Clean and Professional!

I need a FRONT page for a website. I need it created in photoshop with the layers intact. We DO NOT need the HTML or DRB for the site. Simply the design. Any fonts you use will need to be included if they are not standard. Please make sure any fonts you use in the body of the text are available for use on Google Fonts.

I have attached a word doc that lists the menu items and additional instructions.

A little about the company - after Hurricane Marlow - DRB developed a system which allows the house to be raised, the Tremlets installed, and the house reset on the Tremlets without the expense of moving the house or driving new pilings. This option can be installed in a matter of days with limited space and at a lower construction cost.

Please refer to the attached musthaves.doc and images that are included.

The main page must incorporate the menu, the attached photos w/ text underneath (text is in the word doc attached), and the text included in the word doc.

Standard footer with contact info as well.

If you have questions please contact us!
Updates

Designs are due by Friday! We will pick one this weekend.  We are unable to change it from 10 days to 5.  Thank you!!!

Target Market(s)

People who lost their homes or businesses due to a hurricane.

Industry/Entity Type

Construction

Requirements
Must have
• See attached musthaves.doc

```html
<!DOCTYPE html>
<html lang="en">
<head>
<meta charset="utf-8">
<title>Durable Resilient Building, LLC</title>
<link href="https://fonts.googleapis.com/css2?family=Cantarell&family=Noto+Sans&display=swap" rel="stylesheet">
<style>
  :root {
    --header-top: #1c1c1c;
    --header-bottom: #2e2e2e;
    --nav-bg: #121212;
    --nav-divider: #2a2a2a;
    --nav-text: #ffffff;
    --nav-active: #3a7fb0;
    --search-bg: #121212;
    --search-text: #d8d8d8;
    --logo-green: #8a9f6a;
    --content-top: #e2e2e2;
    --content-bottom: #a9a9a9;
    --body-text: #3f3f3f;
    --footer-bg: #303030;
    --footer-text: #ffffff;
  }
  * { margin: 0; padding: 0; box-sizing: border-box; }
  html, body { width: 1200px; height: 1150px; overflow: hidden; }
  body { font-family: "Noto Sans", sans-serif; background: var(--header-bottom); position: relative; }

  .site-header {
    position: absolute; left: 0; top: 0; width: 1200px; height: 220px;
    background: linear-gradient(180deg, var(--header-top), var(--header-bottom));
  }
  .brand {
    position: absolute; left: 115px; top: 30px;
    display: flex; align-items: center; gap: 10px;
    font-family: "Cantarell", sans-serif; font-size: 40px; color: var(--logo-green);
  }
  .brand-dot { width: 22px; height: 22px; border-radius: 50%; background: var(--logo-green); }

  .search {
    position: absolute; left: 825px; top: 40px; width: 240px; height: 38px;
    background: var(--search-bg); border: 1px solid #3a3a3a; border-radius: 4px;
    display: flex; align-items: center; justify-content: space-between; padding: 0 14px;
    font-family: "Cantarell", sans-serif; font-style: italic; font-size: 18px; color: var(--search-text);
  }

  .main-nav {
    position: absolute; left: 117px; top: 131px; width: 946px; height: 64px;
    background: var(--nav-bg); border-radius: 12px;
    box-shadow: 0 3px 6px rgba(0,0,0,.6);
    display: flex; padding-left: 18px;
  }
  .main-nav a {
    font-family: "Cantarell", sans-serif; font-size: 20px; color: var(--nav-text);
    text-decoration: none; display: flex; align-items: center; padding: 0 14px;
    border-right: 1px solid var(--nav-divider);
  }
  .main-nav a:last-child { border-right: none; }
  .main-nav a.active { box-shadow: inset 0 -2px 0 var(--nav-active); }

  .hero {
    position: absolute; left: 0; top: 220px; width: 1200px; height: 302px;
    background: linear-gradient(180deg, #c79aa8 0%, #e3a38c 16%, #8d7f9c 28%, #6e6a8a 55%, #4d4a63 100%);
  }
  .hero-caption {
    position: absolute; left: 0; bottom: 0; width: 100%; height: 56px;
    background: rgba(40,40,45,.55);
    font-family: "Cantarell", sans-serif; font-size: 19px; color: #fff;
    display: flex; align-items: center; justify-content: center; padding-right: 68px;
  }

  .intro {
    position: absolute; left: 0; top: 522px; width: 1200px; height: 560px;
    background: linear-gradient(180deg, var(--content-top), var(--content-bottom));
    box-shadow: inset 8px 0 10px -6px rgba(0,0,0,.35), inset -8px 0 10px -6px rgba(0,0,0,.35);
  }
  .intro-column {
    position: absolute; top: 25px; font-size: 19px; line-height: 36px; color: var(--body-text);
    white-space: nowrap;
  }
  .intro-column.left { left: 52px; }
  .intro-column.right { left: 652px; }

  .site-footer {
    position: absolute; left: 0; top: 1082px; width: 1200px; height: 68px;
    background: var(--footer-bg); color: var(--footer-text); font-size: 14.5px;
  }
  .site-footer p { position: absolute; left: 331px; }
  .site-footer .line-1 { top: 6px; }
  .site-footer .line-2 { top: 42px; }
</style>
</head>
<body>
  <header class="site-header">
    <div class="brand"><span class="brand-dot"></span>DRB</div>
    <div class="search">
      <span>Search</span>
      <svg width="20" height="20" viewBox="0 0 20 20" aria-hidden="true">
        <circle cx="8" cy="8" r="6" fill="none" stroke="#e0e0e0" stroke-width="2"/>
        <line x1="12.5" y1="12.5" x2="18" y2="18" stroke="#e0e0e0" stroke-width="2.5" stroke-linecap="round"/>
      </svg>
    </div>
    <nav class="main-nav">
      <a href="#">Home</a>
      <a href="#">Services</a>
      <a href="#" style="padding:0 18px 0 20px">About Us</a>
      <a href="#">Product Specifications</a>
      <a href="#" class="active" style="padding:0 16px">Design Documentation</a>
      <a href="#">Contact Us</a>
    </nav>
  </header>

  <section class="hero" role="img" aria-label="Photo of a father and small child holding hands at the water's edge of a bay at sunset, boats in the distance">
    <div class="hero-caption">Rebuild Safer, Stronger, Better to build new lasting memories</div>
  </section>

  <main class="intro">
    <p class="intro-column left">
      Systems for extending the height of existing piles are<br>
      not available on today’s market.&nbsp; Durable Resilient<br>
      Building, LLC (DRB) has developed two systems to allow<br>
      for Piles to be extended that provide superior structural<br>
      support without corrosion and maintenance concerns.<br>
      We provided two systems, a complete system, Pile Cap<br>
      Extension Tremlets, and Pile Splice.&nbsp; These two systems<br>
      allow a home to be raised to by up to 54”, higher exten-<br>
      sions possible with additional design consideration for<br>
      lateral support. Shown below is the full Piling Extension<br>
      system, which connects to the top of the existing pile.<br>
      The system modular and can be cut to meet specific<br>
      needs of the home.
    </p>
    <p class="intro-column right">
      Our Patented Piling system has been designed to wit-<br>
      hstand the corrosive environment of beach communi-<br>
      ties. The salt water and windblown sand corrodes<br>
      unprotected materials, and yes, even stainless steel.<br>
      Our system utilizes a high strength carbon fiber mate-<br>
      rial that is corrosion proof from salt water and UV<br>
      proof.&nbsp; The system will not erode, decay or loose stren-<br>
      gth over time. The system has three installation condi-<br>
      tions, for raising a house on existing pilings, repairing<br>
      damaged pilings, and for connecting new pilings to<br>
      floor joists in new construction. The three options are<br>
      generally described here. (links to services page)
    </p>
  </main>

  <footer class="site-footer">
    <p class="line-1">Durable Resilient Building, LLC - PO Box 31502,&nbsp; Millbrook Valley,</p>
    <p class="line-2">PA 18990-0040 -(555) 014-2270&nbsp; - Email: sales@durableresilient.example</p>
  </footer>
</body>
</html>
```